Moder Business Card Design for Renewables Business

Need a business card design for my business. We collect & repurpose spent coffee ground from cafes. The cards will be made from recycled paper. Needs to fit our corporate colour scheme of white, green & brown (see logo for colour codes). Eco friendly, modern, intresting & eye catching.
This card needs to convey the message of the business and fit into its mantra of eco-friendly, sustainable etc.

Target Market(s)

Cafe Owners, Coffee Drinkers, Recycling Companies, Farmers

Industry/Entity Type

Recycling

Contact Information for Business Card

Name; Peter Halloran
Phone; 0412 386 527
e-mail; info@lumatrove.com.au
website; www.lumatrove.com.au

Font styles to use
Sans Serif
Script

Colors

Designer to choose colors to be used in the design.

Requirements
Must have
• FRONT;
• Logo, Name (Peter Halloran), phone number, e-mail address, website
• BACK;
• On the back in cursive text; 'SECOND LIFE FOR EVERY LAST BEAN'
• Small facebook & Instagram logos with text 'Lumatrove'
Should not have
• messy design

```html
<!DOCTYPE html>
<html lang="en">
<head>
<meta charset="utf-8">
<title>Lumatrove Business Card</title>
<link href="https://fonts.googleapis.com/css2?family=Arimo:wght@400;700&family=Dancing+Script:wght@600&display=swap" rel="stylesheet">
<style>
  :root {
    --brown: #62301a;
    --green: #79a33a;
    --white: #ffffff;
    --ink: #2b2b2b;
  }
  * { margin: 0; padding: 0; box-sizing: border-box; }
  html, body { width: 900px; height: 1200px; overflow: hidden; background: var(--white); }
  body { position: relative; font-family: "Arimo", Arial, sans-serif; }

  .card { position: absolute; left: 0; width: 900px; height: 554px; }
  .card--front { top: 0; }
  .card--back { top: 646px; }
  .card__shapes { position: absolute; inset: 0; width: 900px; height: 554px; display: block; }

  .brand { position: absolute; left: 40px; width: 290px; top: 140px; text-align: center; }
  .brand__mark {
    width: 118px; height: 118px; margin: 0 auto;
    border-radius: 50%; border: 6px solid var(--brown);
  }
  .brand__name {
    margin-top: 14px; font-size: 22px; font-weight: 400; letter-spacing: 0.5px;
    color: var(--green);
  }
  .person {
    position: absolute; left: 40px; width: 290px; top: 322px; text-align: center;
    font-size: 27px; color: var(--ink); line-height: 1;
  }
  .person__name {
    display: inline-block; padding-bottom: 3px; border-bottom: 2px solid var(--brown);
  }
  .person__name strong { font-weight: 700; }

  .contact { position: absolute; left: 564px; top: 204px; list-style: none; }
  .contact__item {
    display: flex; align-items: center; height: 30px; margin-bottom: 28px;
    color: var(--white); font-weight: 700; font-size: 21px;
  }
  .contact__item:nth-child(2) { margin-bottom: 34px; }
  .contact__icon { width: 28px; height: 28px; margin-right: 8px; flex: none; }

  .motto {
    position: absolute; left: 10px; width: 440px; top: 262px; text-align: center;
    font-family: "Dancing Script", cursive; font-weight: 600; font-size: 32px;
    color: var(--brown); white-space: nowrap;
  }

  .social { position: absolute; left: 577px; top: 222px; list-style: none; }
  .social__item {
    display: flex; align-items: center; height: 44px; margin-bottom: 29px;
    color: var(--white); font-weight: 700; font-size: 37px;
  }
  .social__square {
    width: 42px; height: 42px; margin-right: 18px; flex: none;
    border: 3px solid var(--brown); border-radius: 4px;
  }
</style>
</head>
<body>

<section class="card card--front">
  <svg class="card__shapes" viewBox="0 0 1055 650" preserveAspectRatio="none" aria-hidden="true">
    <rect width="1055" height="650" fill="var(--brown)"/>
    <polygon points="0,128 718,128 640,328 718,523 0,523" fill="var(--white)"/>
    <polygon points="438,162 503,162 612,328 503,493 438,493 548,328" fill="var(--brown)"/>
    <polygon points="523,162 697,162 612,288" fill="var(--green)"/>
    <polygon points="612,368 697,493 523,493" fill="var(--green)"/>
  </svg>

  <div class="brand">
    <div class="brand__mark"></div>
    <p class="brand__name">LUMATROVE</p>
  </div>

  <p class="person"><span class="person__name">PETER <strong>HALLORAN</strong></span></p>

  <ul class="contact">
    <li class="contact__item">
      <svg class="contact__icon" viewBox="0 0 28 28" fill="none" stroke="var(--white)" stroke-width="1.6">
        <circle cx="14" cy="14" r="12.5"/>
        <path d="M9.5 8.5c1-1 2-1 2.5 0l1 2c.3.6 0 1.2-.5 1.5l-.8.6c.7 1.6 1.9 2.8 3.5 3.5l.6-.8c.4-.5 1-.7 1.5-.4l2 1c1 .5 1 1.5 0 2.5-1.5 1.5-4 1-6.8-1.7S8 10 9.5 8.5z" fill="var(--white)" stroke="none"/>
      </svg>
      0412 386 527
    </li>
    <li class="contact__item">
      <svg class="contact__icon" viewBox="0 0 28 28" fill="none" stroke="var(--white)" stroke-width="1.8">
        <rect x="2" y="6" width="24" height="16" fill="var(--white)" stroke="none"/>
        <path d="M2 6l12 9 12-9M2 22l9-8M26 22l-9-8" stroke="var(--brown)"/>
      </svg>
      info@lumatrove.com.au
    </li>
    <li class="contact__item">
      <svg class="contact__icon" viewBox="0 0 28 28" fill="none" stroke="var(--white)" stroke-width="1.4">
        <circle cx="14" cy="14" r="12"/>
        <ellipse cx="14" cy="14" rx="5.5" ry="12"/>
        <path d="M2 14h24M14 2v24M4 8h20M4 20h20"/>
      </svg>
      www.lumatrove.com.au
    </li>
  </ul>
</section>

<section class="card card--back">
  <svg class="card__shapes" viewBox="0 0 1055 650" preserveAspectRatio="none" aria-hidden="true">
    <rect width="1055" height="650" fill="var(--brown)"/>
    <polygon points="0,127 718,127 640,323 718,522 0,522" fill="var(--white)"/>
    <polygon points="438,159 503,159 612,323 503,488 438,488 548,323" fill="var(--brown)"/>
    <polygon points="523,159 1055,159 1055,488 523,488 648,323" fill="var(--green)"/>
  </svg>

  <p class="motto">‘Second Life For Every Last Bean’</p>

  <ul class="social">
    <li class="social__item"><span class="social__square"></span>Lumatrove</li>
    <li class="social__item"><span class="social__square"></span>Lumatrove</li>
  </ul>
</section>

</body>
</html>
```